Menu Board 1000mmx500mm re-design

I would like to re-design exiting menu board 1000mmx500mm. Current board letters are bit to small to read. I would like to have pictures (attached) of the food offered on it and at the same time to create balance between pictures and size of the text to be easily readable. Fonts and colours are up to designer choice but prefer warm and bright colours rather anything dark.

Target Market(s)

Food industry

Industry/Entity Type

Food

Font styles to use
Other font styles liked:
• I leave font choice to designer

Colors
FFC000
F8CF3A
FAE287
FDF2CF
FEFAEE
F0912C
F2A743
F7CA91
FBE8D2
FDF5EE
EE7325
F08F49
F5BC92
FAE3D3
FDF4ED

Requirements
Must have
• Pictures + Text
Nice to have
• Balance between images and text.
Should not have
• Can't think of any

```html
<!DOCTYPE html>
<html lang="en">
<head>
<meta charset="utf-8">
<title>Restaurant Menu Board</title>
<link href="https://fonts.googleapis.com/css2?family=Oswald:wght@600;700&family=Montserrat:ital,wght@0,600;0,700;0,800;0,900;1,500&display=swap" rel="stylesheet">
<style>
  :root{
    --cream:#FEFAEE;
    --amber:#FFA800;
    --yellow:#FFC000;
    --orange:#EE7325;
    --red-orange:#F05A1E;
    --brown:#2E1A12;
    --text:#3B2A22;
    --line:#5a4a42;
    --page:#FFFFFF;
  }
  *{margin:0;padding:0;box-sizing:border-box}
  html,body{width:1173px;height:1200px;overflow:hidden;background:var(--page)}
  .menu-board{position:absolute;left:236px;top:20px;width:700px;height:1160px;background:var(--cream);overflow:hidden;font-family:'Montserrat',sans-serif;color:var(--text)}
  .abs{position:absolute}
  .title-top{right:40px;top:50px;font-family:'Oswald',sans-serif;font-weight:700;font-size:100px;line-height:1;color:var(--orange);letter-spacing:1px}
  .title-main{right:36px;top:150px;font-family:'Montserrat',sans-serif;font-weight:900;font-size:128px;line-height:1;color:var(--brown);letter-spacing:-2px}
  .item{width:290px}
  .item-head{display:flex;justify-content:space-between;align-items:flex-end}
  .item-name{font-weight:800;font-size:23px;text-transform:uppercase;color:var(--brown);background:linear-gradient(transparent 62%,var(--red-orange) 62%,var(--red-orange) 88%,transparent 88%);padding:0 2px;letter-spacing:.3px}
  .item-name.tight{letter-spacing:-1px;font-size:22px}
  .price{font-weight:800;font-size:24px;color:var(--red-orange)}
  .desc{font-style:italic;font-weight:500;font-size:13.5px;line-height:1.2;margin-top:10px;color:var(--text)}
  .desc em{color:var(--red-orange);font-weight:700}
  .rule{border-top:2px dashed var(--line);height:0}
  .divider{border-left:2px dashed var(--line);width:0}
  .sauces-title{left:0;width:700px;top:872px;text-align:center;font-weight:900;font-size:36px;color:var(--brown)}
  .sauces-title span{background:linear-gradient(transparent 65%,var(--red-orange) 65%,var(--red-orange) 90%,transparent 90%);padding:0 6px;letter-spacing:1px}
  .sauce-row{display:flex;gap:28px;font-weight:800;font-size:21px;color:var(--red-orange);text-transform:uppercase}
  .badge{display:flex;align-items:center;justify-content:center;text-align:center;border-radius:50%;font-family:'Oswald',sans-serif;font-weight:600;line-height:.95}
  .badge-fresh-top{left:230px;top:300px;width:96px;height:96px;background:var(--yellow);color:var(--brown);font-size:28px;transform:rotate(-12deg)}
  .badge-fresh{left:244px;top:1030px;width:96px;height:96px;background:var(--red-orange);color:#fff;font-size:26px;transform:rotate(-30deg)}
  .tag-extra{left:48px;top:355px;color:#fff;font-family:'Oswald',sans-serif;font-weight:600;font-size:24px;transform:rotate(-45deg)}
  .photo{border-radius:40% 45% 45% 40%}
</style>
</head>
<body>
<main class="menu-board">
  <svg class="abs" style="left:0;top:0" width="700" height="1160" viewBox="0 0 700 1160" aria-hidden="true">
    <path d="M0 0 H170 C120 40 150 90 110 140 C70 190 130 230 80 280 C50 310 20 330 0 340 Z" fill="var(--amber)"/>
    <circle cx="140" cy="80" r="24" fill="var(--amber)"/>
    <path d="M20 380 C40 300 150 270 240 300 C330 330 330 460 250 510 C180 550 60 540 30 490 C10 460 10 420 20 380 Z" fill="var(--red-orange)"/>
    <circle cx="70" cy="560" r="8" fill="var(--red-orange)"/>
    <circle cx="300" cy="520" r="12" fill="var(--red-orange)"/>
    <ellipse cx="580" cy="995" rx="26" ry="11" fill="var(--amber)"/>
    <path d="M300 1030 C380 990 470 1000 540 990 C620 980 680 990 700 1010 V1160 H0 V1080 C100 1090 200 1070 300 1030 Z" fill="var(--amber)"/>
    <path d="M180 1160 C220 1120 280 1100 340 1110 L420 1160 Z" fill="var(--red-orange)"/>
    <line x1="118" y1="860" x2="560" y2="860" stroke="var(--line)" stroke-width="2" stroke-dasharray="7 5"/>
  </svg>

  <h1 class="abs title-top">RESTAURANT</h1>
  <div class="abs title-main">MENU</div>

  <div class="abs photo" role="img" aria-label="Grilled chicken wrap cut in half on a wooden board" style="left:0;top:350px;width:345px;height:160px;background:radial-gradient(ellipse at 50% 40%,#f3e6cc 0%,#d8b98a 55%,#b4733a 100%);transform:rotate(-8deg)"></div>
  <div class="abs tag-extra">EXTRA</div>
  <div class="abs badge badge-fresh-top">VERY<br>FRESH</div>

  <!-- right column -->
  <div class="abs item" style="left:370px;top:300px">
    <div class="item-head"><span class="item-name">1/4 Chicken Box</span><span class="price">£9</span></div>
    <p class="desc">Roti Chicken, Veggie Rice &amp; Salad</p>
  </div>
  <div class="abs rule" style="left:370px;top:372px;width:300px"></div>
  <div class="abs item" style="left:370px;top:395px">
    <div class="item-head"><span class="item-name">1/2 Chicken Box</span><span class="price">£14</span></div>
    <p class="desc">Roti Chicken, Veggie Rice &amp; Salad</p>
  </div>
  <div class="abs rule" style="left:370px;top:467px;width:300px"></div>
  <div class="abs item" style="left:370px;top:490px">
    <div class="item-head"><span class="item-name tight">Roasted Potatoes</span><span class="price">£2.5</span></div>
    <p class="desc">Thyme &amp; Garlic</p>
  </div>
  <div class="abs rule" style="left:370px;top:562px;width:300px"></div>
  <div class="abs item" style="left:370px;top:585px">
    <div class="item-head"><span class="item-name">Water</span><span class="price">£1</span></div>
  </div>
  <div class="abs rule" style="left:370px;top:638px;width:300px"></div>
  <div class="abs item" style="left:370px;top:660px">
    <div class="item-head"><span class="item-name">Can &amp; Juices</span><span class="price">£1.8</span></div>
  </div>
  <div class="abs" role="img" aria-label="Canned soft drinks, glasses of juice and sliced citrus fruit" style="left:370px;top:710px;width:310px;height:130px;border-radius:12px;background:linear-gradient(90deg,#f39a2a 0%,#d62a1e 30%,#3aa7d8 50%,#7fcf4a 65%,#f7c23a 82%,#8ccf3a 100%)"></div>

  <div class="abs divider" style="left:336px;top:495px;height:345px"></div>

  <!-- left column -->
  <div class="abs item" style="left:30px;top:590px">
    <div class="item-head"><span class="item-name">Ciabatta</span><span class="price">£6</span></div>
    <p class="desc">Roti Chicken, Rucola, Caramelized Onions, Tomato, Fresh Onion</p>
  </div>
  <div class="abs rule" style="left:30px;top:668px;width:290px"></div>
  <div class="abs item" style="left:30px;top:688px">
    <div class="item-head"><span class="item-name">Wrap</span><span class="price">£7</span></div>
    <p class="desc">Roti Chicken, Crunchy Slaw, Tomato, Fresh Onion &amp; <em>Sauce of your choice</em></p>
  </div>
  <div class="abs rule" style="left:30px;top:766px;width:290px"></div>
  <div class="abs item" style="left:30px;top:786px">
    <div class="item-head"><span class="item-name">Beetroot Wrap</span><span class="price">£8</span></div>
    <p class="desc">Roti Chicken, Crunchy Slaw, Tomato, Fresh Onion &amp; <em>Sauce of your choice</em></p>
  </div>

  <!-- sauces -->
  <div class="abs" role="img" aria-label="Beetroot wraps filled with chicken and salad" style="left:0;top:855px;width:140px;height:115px;border-radius:30% 50% 50% 20%;background:linear-gradient(135deg,#e9e2cf 0%,#9fbf6a 40%,#a8324a 75%,#7a1f35 100%)"></div>
  <h2 class="abs sauces-title"><span>SAUCES</span></h2>
  <div class="abs sauce-row" style="left:170px;top:945px"><span>Signature</span><span>BBQ</span><span>Piri Piri</span></div>
  <div class="abs sauce-row" style="left:152px;top:975px"><span>Sweet Chilli</span><span>Garlic</span><span>Mayo</span></div>

  <!-- bottom food -->
  <div class="abs" role="img" aria-label="Roasted potatoes with mushrooms and herbs in a dark pan" style="left:0;top:1060px;width:300px;height:100px;border-radius:0 60% 0 0;background:radial-gradient(ellipse at 40% 60%,#e3a45a 0%,#b8652a 55%,#5a3420 100%)"></div>
  <div class="abs" role="img" aria-label="Roast chicken leg with vegetable rice on a wooden plate" style="left:300px;top:1010px;width:420px;height:180px;border-radius:50% 50% 0 0;background:radial-gradient(ellipse at 30% 45%,#d9902f 0%,#b5652a 35%,#f3efe4 60%,#8a4a22 100%)"></div>
  <div class="abs badge badge-fresh">FRESH</div>
</main>
</body>
</html>
```